Postcard and Door Hanger Design

We need two pieces designed for marketing. Both will use the same logo and photo just the text will be slightly different. We need these designs looking very modern, clean, and simple while having the important information to stand out.

Postcard: 2 sided
- Side 1 just have large logo with our website and phone number
- Side 2 below.
- 4 x 6
- Use photo of house provided
- "Going Above and Beyond Every Time"
- "Call TODAY to Reserve your project by May 1st and receive 10% off"
- "Residential and Commercial"
- Our contact is 250-555-0147
- Website is www.brightoakcoatings.com
- Might include something like "check out our portfolio on our website"

Use the above as a guidline and be creative with it, add or take away as you see fit as we are open to suggestions.

Door Hanger: 2 sided
Side 1 - Logo with contact details
Side 2 - Below
- 4 x 11
- "We are painting your neighborhood"
-"come see us in action at (then leave a space where we can stick a label onto our door hanger with an address of a home we are painting)
- Call today for a FREE ESTIMATE
- 250-555-0147
- www.brightoakcoatings.com

https://www.filenook.net/sh/42qrt19k3mzp5xa/RT7KLMN-QZ

https://www.filenook.net/sh/tt3ru58w7jxe21c/LMwRRJnoQx

https://www.filenook.net/sh/p3z55rf6wqn44dd/xvt-Hj2KWa

```html
<!DOCTYPE html>
<html lang="en">
<head>
<meta charset="utf-8">
<title>BrightOak Coatings Postcard</title>
<link rel="stylesheet" href="https://fonts.googleapis.com/css2?family=Cinzel:wght@400&family=Open+Sans:wght@400;600&display=swap">
<style>
  :root {
    --backdrop: #2e3a42;
    --card: #25323b;
    --teal: #3fb4b4;
    --white: #ffffff;
    --soft-white: #e6ecef;
    --photo-light: #b9a48a;
    --photo-mid: #7a6654;
    --photo-dark: #3b3029;
  }
  * { margin: 0; padding: 0; box-sizing: border-box; }
  html, body {
    width: 1200px; height: 900px; overflow: hidden;
    background: var(--backdrop);
    font-family: "Open Sans", Arial, sans-serif;
  }
  .card {
    position: absolute; left: 273px; width: 618px; height: 412px;
    background: var(--card);
    box-shadow: 0 4px 14px rgba(0,0,0,0.35);
    overflow: hidden;
  }
  .card--front { top: 30px; }
  .card--back { top: 463px; }

  .front-stripes { position: absolute; inset: 0; }

  .brand { position: absolute; text-align: center; }
  .brand__mark { display: block; margin: 0 auto; background: var(--teal); }
  .brand__name {
    font-family: "Cinzel", Georgia, serif; font-weight: 400;
    color: var(--teal); line-height: 1; white-space: nowrap;
  }
  .brand__sub {
    font-family: "Cinzel", Georgia, serif; font-weight: 400;
    color: var(--teal); line-height: 1; white-space: nowrap;
  }

  .card--front .brand { left: 0; width: 620px; top: 150px; }
  .card--front .brand__mark { width: 30px; height: 30px; margin-bottom: 56px; }
  .card--front .brand__name { font-size: 25px; letter-spacing: 2px; }
  .card--front .brand__sub { font-size: 11px; letter-spacing: 8px; margin-top: 7px; }

  .phone {
    display: flex; align-items: center; gap: 6px;
    color: var(--white); white-space: nowrap;
  }
  .phone__icon { flex: none; }
  .card--front .phone {
    position: absolute; top: 279px; left: 0; width: 620px;
    justify-content: center; font-size: 15px;
  }

  .photo {
    position: absolute; inset: 0;
    background: linear-gradient(160deg, var(--photo-light) 0%, var(--photo-mid) 45%, var(--photo-dark) 100%);
    clip-path: polygon(264px 0, 618px 0, 618px 412px, 185px 412px);
  }
  .segments {
    position: absolute; left: 21px; top: 17px;
    color: var(--soft-white); font-size: 13.5px; line-height: 17px;
    text-transform: uppercase;
  }
  .card--back .brand { left: 0; width: 206px; top: 100px; }
  .card--back .brand__mark { width: 30px; height: 30px; margin-bottom: 50px; }
  .card--back .brand__name { font-size: 22px; letter-spacing: 1.5px; }
  .card--back .brand__sub { font-size: 9px; letter-spacing: 6px; margin-top: 6px; }

  .offer {
    position: absolute; left: 24px; top: 307px;
    color: var(--soft-white); font-size: 12.5px; line-height: 15.5px;
    text-transform: uppercase;
  }
  .offer em { font-style: normal; color: var(--teal); }

  .headline {
    position: absolute; left: 310px; width: 304px; top: 103px;
    font-family: "Cinzel", Georgia, serif; font-weight: 400;
    color: var(--teal); font-size: 33px; line-height: 41px;
    text-align: center; text-transform: uppercase; white-space: nowrap;
  }
  .card--back .phone {
    position: absolute; top: 310px; right: 24px; font-size: 18px;
  }
  .web {
    position: absolute; right: 24px; top: 351px; text-align: right;
    color: var(--white); white-space: nowrap;
  }
  .web__url { font-size: 13px; font-weight: 600; letter-spacing: 0.5px; line-height: 16px; }
  .web__note { font-size: 11px; line-height: 14px; color: var(--soft-white); }
</style>
</head>
<body>

<section class="card card--front">
  <svg class="front-stripes" width="618" height="412" viewBox="0 0 618 412" aria-hidden="true">
    <polygon points="618,135 618,152 429,412 416,412" fill="#ffffff"/>
    <polygon points="618,165 618,182 454,412 441,412" fill="#ffffff"/>
  </svg>
  <div class="brand">
    <span class="brand__mark"></span>
    <div class="brand__name">BRIGHTOAK</div>
    <div class="brand__sub">COATINGS</div>
  </div>
  <div class="phone">
    <svg class="phone__icon" width="12" height="12" viewBox="0 0 12 12" aria-hidden="true">
      <rect width="12" height="12" rx="2" fill="#ffffff"/>
      <path d="M3.6 2.6l1.3 0 .6 1.8-.9.7c.4.9 1.1 1.6 2 2l.7-.9 1.8.6v1.3c0 .4-.3.6-.7.6C5.6 8.5 3.5 6.4 3 3.3c0-.4.2-.7.6-.7z" fill="#25323b"/>
    </svg>
    <span>250-555-0147</span>
  </div>
</section>

<section class="card card--back">
  <div class="photo" role="img" aria-label="Photo of a freshly painted modern kitchen with island, bar stools and coffered ceiling"></div>

  <div class="segments">Residential<br>and Commercial</div>

  <div class="brand">
    <span class="brand__mark"></span>
    <div class="brand__name">BRIGHTOAK</div>
    <div class="brand__sub">COATINGS</div>
  </div>

  <p class="offer">
    Call <em>Today</em><br>
    to <em>Reserve</em><br>
    your <em>Project</em><br>
    by May 1st<br>
    and <em>Receive 10% off</em>
  </p>

  <h1 class="headline">Going Above<br>and Beyond<br>Every Time</h1>

  <div class="phone">
    <svg class="phone__icon" width="14" height="14" viewBox="0 0 12 12" aria-hidden="true">
      <rect width="12" height="12" rx="2" fill="#ffffff"/>
      <path d="M3.6 2.6l1.3 0 .6 1.8-.9.7c.4.9 1.1 1.6 2 2l.7-.9 1.8.6v1.3c0 .4-.3.6-.7.6C5.6 8.5 3.5 6.4 3 3.3c0-.4.2-.7.6-.7z" fill="#25323b"/>
    </svg>
    <span>250-555-0147</span>
  </div>

  <div class="web">
    <div class="web__url">www.brightoakcoatings.com</div>
    <div class="web__note">check out our portfolio on our website</div>
  </div>
</section>

</body>
</html>
```